NEW Household Invention Needs a Package Design!

We need a 'retail' package design for a new product invented for the household kitchen market. Brimloft has developed a reusable food storage system that can be tailored to an individual's needs and have a sustainable impact on their ability to make good dietary decisions, while helping save the planet. We would like to see designs that use the brand's branding guidelines and logo. The final design should communicate the key features of the product (patented customizable modular system, fill lines, collapsible functionality and sustainable materials), as well as, all other notable aspects (Microwave/Dishwasher Safe, Leakproof, 100% BPA Free, Donates 1% of purchase price, etc.). It's important that the benefits of the product are well highlighted (More variety to better balance nutrition, More easily stored in bag, kitchen cabinet or drawer and Ends waste)
Updates

Hi All, we are looking for a package design for retail, something that will be on a shelf in our product category.

Target Market(s)

Health conscious men and women who have a passion for nutrition & social responsibility, operate a lifestyle on-the-go and monitor their spending by preparing meals at home.

Industry/Entity Type

Food Tech, Consumer Products, Health & Wellness

Font styles to use
Other font styles liked:
• See Brand Guidelines

Requirements
Must have
• Follow brand guidelines: https://guidelines.quorvadesign.example/brimloft/guidelines/

```html
<!DOCTYPE html>
<html lang="en">
<head>
<meta charset="utf-8">
<title>Brimloft container set cartons</title>
<link rel="stylesheet" href="https://fonts.googleapis.com/css2?family=Montserrat:wght@500;600;700;800&display=swap">
<style>
:root{
  --kraft:#d7c7aa;
  --crease:#6e604c;
  --white:#ffffff;
  --coral:#f5a08a;
  --coral-deep:#e97f66;
  --sky:#a9d8f3;
  --sky-deep:#5fb4e4;
  --lime:#c6d98e;
  --lime-deep:#86c25a;
  --plum:#7c1f5e;
  --berry:#e9485e;
}
*{box-sizing:border-box;margin:0;padding:0}
html,body{width:1023px;height:1200px;overflow:hidden;background:var(--white)}
body{position:relative;font-family:"Montserrat",Arial,sans-serif;color:var(--white)}
.carton{position:absolute;width:261px;height:1072px;background:var(--kraft);border:1px solid var(--crease)}
.carton--verve{left:51px;top:59px}
.carton--atlas{left:375px;top:51px}
.carton--nook{left:711px;top:51px}
.crease{position:absolute;left:0;right:0;height:0;border-top:1px solid var(--crease)}
.crease--1{top:72px}.crease--2{top:537px}.crease--3{top:608px}
.abs{position:absolute}
.brand{font-weight:700;letter-spacing:-.5px;line-height:1}
.front .brand{left:14px;top:94px;font-size:33px}
.front .title{left:18px;top:178px;font-size:29px;font-weight:800;line-height:1}
.front .subtitle{left:18px;top:210px;font-size:12.5px;font-weight:700}
.front .tagline{left:18px;top:226px;font-size:5.6px;font-weight:700;line-height:1.35}
.hero{left:0;top:254px;width:259px;height:184px}
.hero--verve{background:radial-gradient(ellipse at 50% 55%,#fbe9e2 0%,var(--coral-deep) 45%,var(--coral) 75%)}
.hero--atlas{background:radial-gradient(ellipse at 50% 55%,#eef5f7 0%,var(--sky-deep) 45%,var(--sky) 75%)}
.hero--nook{background:radial-gradient(ellipse at 50% 55%,#f1f4ea 0%,var(--lime-deep) 45%,var(--lime) 75%)}
.seal{left:180px;top:223px;width:61px;height:61px;border-radius:50%;background:var(--plum)}
.icons{display:flex;position:absolute}
.front .icons{left:131px;top:458px;gap:7px}
.icon{width:31px;height:52px;border:1px solid var(--white);border-radius:3px;display:flex;flex-direction:column;align-items:center;padding-top:6px}
.icon svg{width:15px;height:13px;fill:none;stroke:var(--white);stroke-width:1.1}
.icon span{margin-top:auto;margin-bottom:6px;font-size:4.3px;font-weight:600;text-align:center;line-height:1.2}
.charity{left:131px;top:628px;width:110px;height:27px;background:var(--white);border-radius:4px;display:flex;align-items:center;gap:5px;padding:0 5px}
.charity .hands{width:17px;height:17px;border:1px solid var(--kraft);border-radius:50%;flex:none}
.charity p{font-size:4.2px;font-weight:600;color:#c3b294;line-height:1.25}
.back .brand{left:17px;top:665px;font-size:28px}
.back .title{left:18px;top:703px;font-size:17px;font-weight:700;line-height:1}
.back .subtitle{left:18px;top:721px;font-size:9.5px;font-weight:700}
.back .story{left:18px;top:734px;width:110px;font-size:5.3px;font-weight:600;line-height:1.3}
.back .story p+p{margin-top:6px}
.back .specs{left:136px;top:712px;width:110px;font-size:5.7px;font-weight:600;line-height:1.2}
.specs p{margin-bottom:7px}
.tray{position:absolute;left:52px;width:44px;height:30px;border:1px solid var(--white);border-radius:3px}
.art{left:49px;top:817px;width:188px;height:86px;border:1px solid rgba(255,255,255,.85);border-radius:0 0 14px 14px;background:linear-gradient(100deg,#c92c2c 0%,#e3704a 40%,#7d2f6f 65%,#6a9a3f 100%);opacity:.85}
.bubble{left:196px;top:810px;width:42px;height:42px;border-radius:50%;background:var(--berry)}
.rule{position:absolute;left:18px;width:225px;border-top:1px solid rgba(255,255,255,.8)}
.back .icons{left:20px;top:918px;gap:7.5px}
.divider{left:128px;top:985px;height:42px;border-left:1px solid rgba(255,255,255,.8)}
.code-panel{left:166px;top:990px;width:78px;height:38px;background:var(--white)}
</style>
</head>
<body>

<!-- Verve -->
<section class="carton carton--verve">
  <div class="crease crease--1"></div><div class="crease crease--2"></div><div class="crease crease--3"></div>
  <div class="front">
    <div class="abs brand">Brimloft</div>
    <h1 class="abs title">The Verve</h1>
    <div class="abs subtitle">container set</div>
    <p class="abs tagline">The ideal lunchbox for the on-the-go lifestyle.<br>Pack a balanced meal, perfectly portioned.</p>
    <div class="abs hero hero--verve" role="img" aria-label="Photo of coral collapsible lunch containers filled with a balanced meal"></div>
    <div class="abs seal"></div>
    <div class="icons">
      <div class="icon"><svg viewBox="0 0 15 13"><rect x="1" y="2" width="13" height="9"/><rect x="3" y="4" width="7" height="5"/></svg><span>Microwave/<br>Dishwasher<br>Safe</span></div>
      <div class="icon"><svg viewBox="0 0 15 13"><path d="M5 2c-2 3-3 5-3 6a3 3 0 006 0c0-1-1-3-3-6z"/><path d="M1 12L14 1"/></svg><span>Leakproof</span></div>
      <div class="icon"><svg viewBox="0 0 15 13"><path d="M2 12C3 5 8 2 13 1c0 6-4 10-10 10z"/><path d="M2 12l7-7"/></svg><span>100%<br>BPA<br>Free</span></div>
    </div>
  </div>
  <div class="back">
    <div class="abs charity"><div class="hands"></div><p>WITH EVERY CONTAINER SOLD, 1% OF THE PURCHASE PRICE WILL BE DONATED TO THE ASSOCIATED CHARITY.</p></div>
    <div class="abs brand">Brimloft</div>
    <h2 class="abs title">The Verve</h2>
    <div class="abs subtitle">container set</div>
    <div class="abs story"><p>The ideal lunchbox for the on-the-go lifestyle. Pack a balanced meal, perfectly portioned.</p><p>Terrific for salads, pastas, stews, there are no limits. Pack your favorite balanced meal with this perfectly portioned food storage container set. Then collapse and stow away for a more convenient carrying size.</p></div>
    <div class="abs specs"><p>6 Pieces | 1 Utensil<br>3 Compartment</p><p>Large Compartment<br>Volume<br>24oz<br>709.8ml</p><p>Small Compartments<br>Volume<br>8oz<br>236.7ml</p><div class="tray" style="top:24px"></div></div>
    <div class="abs art" role="img" aria-label="Illustration of a red pepper, beetroot and carrot inside a container outline"></div>
    <div class="abs bubble"></div>
    <div class="rule" style="top:907px"></div>
    <div class="icons">
      <div class="icon"><svg viewBox="0 0 15 13"><rect x="1" y="2" width="13" height="9"/><rect x="3" y="4" width="7" height="5"/></svg><span>Microwave<br>Safe</span></div>
      <div class="icon"><svg viewBox="0 0 15 13"><rect x="3" y="0.5" width="9" height="12"/><circle cx="7.5" cy="7.5" r="2.5"/></svg><span>Dishwasher<br>Safe</span></div>
      <div class="icon"><svg viewBox="0 0 15 13"><rect x="3" y="0.5" width="9" height="12"/><path d="M7.5 4v7M4.5 7.5h6M5.5 5.5l4 4M9.5 5.5l-4 4"/></svg><span>Freezer<br>Safe</span></div>
      <div class="icon"><svg viewBox="0 0 15 13"><path d="M1 5l6-3 7 3-7 3z"/><path d="M1 5v4l6 3 7-3V5"/></svg><span>Airtight</span></div>
      <div class="icon"><svg viewBox="0 0 15 13"><path d="M5 2c-2 3-3 5-3 6a3 3 0 006 0c0-1-1-3-3-6z"/><path d="M1 12L14 1"/></svg><span>Leakproof</span></div>
      <div class="icon"><svg viewBox="0 0 15 13"><path d="M2 12C3 5 8 2 13 1c0 6-4 10-10 10z"/><path d="M2 12l7-7"/></svg><span>100%<br>BPA<br>Free</span></div>
    </div>
    <div class="rule" style="top:978px"></div>
    <div class="abs divider"></div>
    <div class="abs code-panel"></div>
  </div>
</section>

<!-- Atlas -->
<section class="carton carton--atlas">
  <div class="crease crease--1"></div><div class="crease crease--2"></div><div class="crease crease--3"></div>
  <div class="front">
    <div class="abs brand">Brimloft</div>
    <h1 class="abs title">The Atlas</h1>
    <div class="abs subtitle">container set</div>
    <p class="abs tagline">The ideal lunchbox for the on-the-go lifestyle.<br>Pack a balanced meal, perfectly portioned.</p>
    <div class="abs hero hero--atlas" role="img" aria-label="Photo of blue collapsible lunch containers filled with a balanced meal"></div>
    <div class="abs seal"></div>
    <div class="icons">
      <div class="icon"><svg viewBox="0 0 15 13"><rect x="1" y="2" width="13" height="9"/><rect x="3" y="4" width="7" height="5"/></svg><span>Microwave/<br>Dishwasher<br>Safe</span></div>
      <div class="icon"><svg viewBox="0 0 15 13"><path d="M5 2c-2 3-3 5-3 6a3 3 0 006 0c0-1-1-3-3-6z"/><path d="M1 12L14 1"/></svg><span>Leakproof</span></div>
      <div class="icon"><svg viewBox="0 0 15 13"><path d="M2 12C3 5 8 2 13 1c0 6-4 10-10 10z"/><path d="M2 12l7-7"/></svg><span>100%<br>BPA<br>Free</span></div>
    </div>
  </div>
  <div class="back">
    <div class="abs charity"><div class="hands"></div><p>WITH EVERY CONTAINER SOLD, 1% OF THE PURCHASE PRICE WILL BE DONATED TO THE ASSOCIATED CHARITY.</p></div>
    <div class="abs brand">Brimloft</div>
    <h2 class="abs title">The Atlas</h2>
    <div class="abs subtitle">container set</div>
    <div class="abs story"><p>Pack the right amount of nourishment to keep you sharp at the office, or dominate that workout.<br>The name explains it all. Adding this food storage container set to support all the hard work you put cooking in the kitchen, will go down in history as the best food storage purchase.<br>Suitable for any meal, the Atlas balances both size and variety for your next trip to the office, gym or daily activity where you need nourishment.</p></div>
    <div class="abs specs"><p>6 Pieces | 1 Utensil<br>3 Compartment</p><p>Large Compartment<br>Volume<br>24oz<br>709.8ml</p><p>Small Compartments<br>Volume<br>8oz<br>236.7ml</p><div class="tray" style="top:24px"></div></div>
    <div class="abs art" role="img" aria-label="Illustration of a red pepper, beetroot and carrot inside a container outline"></div>
    <div class="abs bubble"></div>
    <div class="rule" style="top:907px"></div>
    <div class="icons">
      <div class="icon"><svg viewBox="0 0 15 13"><rect x="1" y="2" width="13" height="9"/><rect x="3" y="4" width="7" height="5"/></svg><span>Microwave<br>Safe</span></div>
      <div class="icon"><svg viewBox="0 0 15 13"><rect x="3" y="0.5" width="9" height="12"/><circle cx="7.5" cy="7.5" r="2.5"/></svg><span>Dishwasher<br>Safe</span></div>
      <div class="icon"><svg viewBox="0 0 15 13"><rect x="3" y="0.5" width="9" height="12"/><path d="M7.5 4v7M4.5 7.5h6M5.5 5.5l4 4M9.5 5.5l-4 4"/></svg><span>Freezer<br>Safe</span></div>
      <div class="icon"><svg viewBox="0 0 15 13"><path d="M1 5l6-3 7 3-7 3z"/><path d="M1 5v4l6 3 7-3V5"/></svg><span>Airtight</span></div>
      <div class="icon"><svg viewBox="0 0 15 13"><path d="M5 2c-2 3-3 5-3 6a3 3 0 006 0c0-1-1-3-3-6z"/><path d="M1 12L14 1"/></svg><span>Leakproof</span></div>
      <div class="icon"><svg viewBox="0 0 15 13"><path d="M2 12C3 5 8 2 13 1c0 6-4 10-10 10z"/><path d="M2 12l7-7"/></svg><span>100%<br>BPA<br>Free</span></div>
    </div>
    <div class="rule" style="top:978px"></div>
    <div class="abs divider"></div>
    <div class="abs code-panel"></div>
  </div>
</section>

<!-- Nook -->
<section class="carton carton--nook">
  <div class="crease crease--1"></div><div class="crease crease--2"></div><div class="crease crease--3"></div>
  <div class="front">
    <div class="abs brand">Brimloft</div>
    <h1 class="abs title">The Nook</h1>
    <div class="abs subtitle">container set</div>
    <p class="abs tagline">The ideal lunchbox for the on-the-go lifestyle.<br>Pack a balanced meal, perfectly portioned.</p>
    <div class="abs hero hero--nook" role="img" aria-label="Photo of green collapsible two-compartment lunch container with a balanced meal"></div>
    <div class="abs seal"></div>
    <div class="icons">
      <div class="icon"><svg viewBox="0 0 15 13"><rect x="1" y="2" width="13" height="9"/><rect x="3" y="4" width="7" height="5"/></svg><span>Microwave/<br>Dishwasher<br>Safe</span></div>
      <div class="icon"><svg viewBox="0 0 15 13"><path d="M5 2c-2 3-3 5-3 6a3 3 0 006 0c0-1-1-3-3-6z"/><path d="M1 12L14 1"/></svg><span>Leakproof</span></div>
      <div class="icon"><svg viewBox="0 0 15 13"><path d="M2 12C3 5 8 2 13 1c0 6-4 10-10 10z"/><path d="M2 12l7-7"/></svg><span>100%<br>BPA<br>Free</span></div>
    </div>
  </div>
  <div class="back">
    <div class="abs charity"><div class="hands"></div><p>WITH EVERY CONTAINER SOLD, 1% OF THE PURCHASE PRICE WILL BE DONATED TO THE ASSOCIATED CHARITY.</p></div>
    <div class="abs brand">Brimloft</div>
    <h2 class="abs title">The Nook</h2>
    <div class="abs subtitle">container set</div>
    <div class="abs story"><p>A compact carrying case for the “snacker” in all of us. Some call it “snacktastic.”</p><p>The Nook was created to balance size and carrying capacity in a lightweight and leak proof design. It's the best lunch box, perfect for kids and everyday travel. You can be confident in transporting anything.</p></div>
    <div class="abs specs"><p>4 Pieces | 1 Utensil<br>2 Compartment</p><p>Compartment<br>Volume<br>16oz<br>273.2ml</p><div class="tray" style="top:24px"></div></div>
    <div class="abs art" role="img" aria-label="Illustration of a red pepper, beetroot and carrot inside a container outline"></div>
    <div class="abs bubble"></div>
    <div class="rule" style="top:907px"></div>
    <div class="icons">
      <div class="icon"><svg viewBox="0 0 15 13"><rect x="1" y="2" width="13" height="9"/><rect x="3" y="4" width="7" height="5"/></svg><span>Microwave<br>Safe</span></div>
      <div class="icon"><svg viewBox="0 0 15 13"><rect x="3" y="0.5" width="9" height="12"/><circle cx="7.5" cy="7.5" r="2.5"/></svg><span>Dishwasher<br>Safe</span></div>
      <div class="icon"><svg viewBox="0 0 15 13"><rect x="3" y="0.5" width="9" height="12"/><path d="M7.5 4v7M4.5 7.5h6M5.5 5.5l4 4M9.5 5.5l-4 4"/></svg><span>Freezer<br>Safe</span></div>
      <div class="icon"><svg viewBox="0 0 15 13"><path d="M1 5l6-3 7 3-7 3z"/><path d="M1 5v4l6 3 7-3V5"/></svg><span>Airtight</span></div>
      <div class="icon"><svg viewBox="0 0 15 13"><path d="M5 2c-2 3-3 5-3 6a3 3 0 006 0c0-1-1-3-3-6z"/><path d="M1 12L14 1"/></svg><span>Leakproof</span></div>
      <div class="icon"><svg viewBox="0 0 15 13"><path d="M2 12C3 5 8 2 13 1c0 6-4 10-10 10z"/><path d="M2 12l7-7"/></svg><span>100%<br>BPA<br>Free</span></div>
    </div>
    <div class="rule" style="top:978px"></div>
    <div class="abs divider"></div>
    <div class="abs code-panel"></div>
  </div>
</section>

</body>
</html>
```